Brightwell Comfort Contractors - Ductless Mini-Split Ad Creative Brief 4 qp ad images

Our Offers (Must Be Clearly Visible in the Design)
100% Satisfaction Guarantee
"We guarantee to keep you cool, or your money back! If you're not happy after we’ve had a chance to fix it, we’ll refund you!"

5-Year Labor Warranty
"That’s right – a 5-year labor warranty! No maintenance agreement required, just clean your filters each month!"

Chill-Wave Season 2025
"LIMITED-TIME OFFER: Get $999 off any ductless mini-split installation!"

Transparent Pricing
"What you see is what you pay—NO hidden fees!"

Ad Design Guidelines
Primary Focus: Ductless Mini-Split A/C Systems ONLY
Color Scheme: Must incorporate Brightwell Comfort Contractors' main colors with a hint of yellow to catch attention.
Look at truck wrap to get a feel for the border of ad image creative
Branding Elements: Include Brightwell Comfort logo prominently.
Contact Details: Display phone number clearly.
Trust Builders: Feature Chatterly & Zorvex review elements to enhance credibility.
Visibility: The offers must be clear and readable but not overcrowded. Prioritize readability and clean design.
Final Notes
Ensure the design is high-converting and visually engaging while maintaining a professional, premium feel.
The ad creatives will be used for ductless mini-split A/C systems only—this must be clear in the design messaging.
Feel Free to use your expertise and experience to make this better
Thank you 555-317-2946

```html
<!DOCTYPE html>
<html lang="en">
<head>
<meta charset="utf-8">
<title>Brightwell Comfort Contractors – Ductless Mini-Split Ads</title>
<link href="https://fonts.googleapis.com/css2?family=Poppins:wght@700;800&family=Figtree:wght@400;500&display=swap" rel="stylesheet">
<style>
  :root{
    --page:#585c5f;
    --card:#ffffff;
    --red:#d0232a;
    --blue:#1565c0;
    --ink:#3a3a3a;
  }
  html,body{margin:0;padding:0;width:1200px;height:1200px;overflow:hidden;background:var(--page);}
  .stage{position:absolute;left:0;top:0;width:1932px;height:1932px;transform:scale(0.621118);transform-origin:0 0;}
  .ad{position:absolute;width:817px;height:817px;background:var(--card);overflow:hidden;box-shadow:0 3px 8px rgba(0,0,0,.35);}
  .ad--warranty{left:134px;top:132px;}
  .ad--guarantee{left:984px;top:132px;}
  .ad--season{left:134px;top:987px;}
  .ad--pricing{left:984px;top:987px;}
  .ad__art{position:absolute;left:0;top:0;width:817px;height:817px;}
  .headline{position:absolute;font-family:"Poppins",sans-serif;font-weight:800;margin:0;line-height:1;}
  .body{position:absolute;font-family:"Figtree",sans-serif;font-weight:400;color:var(--ink);margin:0;}
  .red{color:var(--red);} .blue{color:var(--blue);}
  .brand{position:absolute;width:270px;text-align:center;}
  .brand__dot{display:block;width:86px;height:86px;border-radius:50%;background:var(--red);margin:0 auto 18px;}
  .brand__name{font-family:"Poppins",sans-serif;font-weight:800;color:var(--blue);font-size:29px;line-height:1.08;margin:0;}
</style>
</head>
<body>
<div class="stage">

  <!-- Warranty -->
  <section class="ad ad--warranty">
    <svg class="ad__art" viewBox="0 0 817 817">
      <defs><linearGradient id="snow" x1="0" y1="0" x2="0" y2="1"><stop offset="0" stop-color="#cfcbc6"/><stop offset=".55" stop-color="#8a7d70"/><stop offset="1" stop-color="#eef0f3"/></linearGradient></defs>
      <path role="img" aria-label="Photo: four technicians beside two new outdoor mini-split units in the snow" d="M0 0H817V400C600 505 250 495 0 400Z" fill="url(#snow)"/>
      <path d="M0 420C160 480 320 505 520 500" fill="none" stroke="var(--red)" stroke-width="14"/>
      <path d="M40 410C300 515 600 495 817 415" fill="none" stroke="var(--blue)" stroke-width="16"/>
    </svg>
    <p class="headline red" style="left:56px;top:520px;font-size:190px;">5</p>
    <p class="headline blue" style="left:168px;top:537px;font-size:44px;line-height:49px;">Year<br>Labor<br>Warranty</p>
    <p class="body" style="left:60px;top:698px;font-size:19.5px;line-height:23px;">That’s right – a 5-year labor warranty!<br>No maintenance agreement required,<br>just clean your filters each month!</p>
    <div class="brand" style="left:497px;top:575px;"><span class="brand__dot"></span><p class="brand__name">Brightwell Comfort Contractors</p></div>
  </section>

  <!-- Guarantee -->
  <section class="ad ad--guarantee">
    <svg class="ad__art" viewBox="0 0 817 817">
      <defs><linearGradient id="yard" x1="0" y1="0" x2="1" y2="1"><stop offset="0" stop-color="#a89284"/><stop offset=".5" stop-color="#c9c0b2"/><stop offset="1" stop-color="#6c7f95"/></linearGradient></defs>
      <g transform="translate(817 0) scale(-1 1)">
        <path role="img" aria-label="Photo: a happy homeowner with a technician beside her outdoor unit" d="M0 0H817V400C600 505 250 495 0 400Z" fill="url(#yard)"/>
        <path d="M0 420C160 480 320 505 520 500" fill="none" stroke="var(--red)" stroke-width="14"/>
        <path d="M40 410C300 515 600 495 817 415" fill="none" stroke="var(--blue)" stroke-width="16"/>
      </g>
    </svg>
    <p class="headline red" style="left:50px;top:512px;font-size:92px;">100%</p>
    <p class="headline blue" style="left:50px;top:598px;font-size:43px;line-height:46px;">Satisfaction<br>Guarantee</p>
    <p class="body" style="left:50px;top:694px;font-size:19.5px;line-height:23px;">We guarantee to keep you cool, or<br>your money back! If you're not<br>happy after we’ve had a chance to<br>fix it, we’ll refund you!</p>
    <div class="brand" style="left:492px;top:580px;"><span class="brand__dot"></span><p class="brand__name">Brightwell Comfort Contractors</p></div>
  </section>

  <!-- Season offer -->
  <section class="ad ad--season">
    <svg class="ad__art" viewBox="0 0 817 817">
      <defs><linearGradient id="lawn" x1="0" y1="0" x2="1" y2="1"><stop offset="0" stop-color="#d9d4cc"/><stop offset=".55" stop-color="#b99a80"/><stop offset="1" stop-color="#5f8a3e"/></linearGradient></defs>
      <path role="img" aria-label="Photo: technician giving a thumbs up beside an installed mini-split condenser" d="M0 0H817V400C600 505 250 495 0 400Z" fill="url(#lawn)"/>
      <path d="M0 420C160 480 320 505 520 500" fill="none" stroke="var(--red)" stroke-width="14"/>
      <path d="M40 410C300 515 600 495 817 415" fill="none" stroke="var(--blue)" stroke-width="16"/>
    </svg>
    <p class="headline red" style="left:84px;top:565px;font-size:54px;">Chill-Wave</p>
    <p class="headline blue" style="left:84px;top:623px;font-size:46px;">Season 2025</p>
    <p class="body" style="left:88px;top:685px;font-size:24.5px;line-height:28px;">LIMITED-TIME OFFER:<br>Get $999 off any ductless<br>mini-split installation!</p>
    <div class="brand" style="left:507px;top:580px;"><span class="brand__dot"></span><p class="brand__name">Brightwell Comfort Contractors</p></div>
  </section>

  <!-- Pricing -->
  <section class="ad ad--pricing">
    <svg class="ad__art" viewBox="0 0 817 817">
      <defs><linearGradient id="stone" x1="0" y1="0" x2="1" y2="1"><stop offset="0" stop-color="#7a6248"/><stop offset=".5" stop-color="#b59a78"/><stop offset="1" stop-color="#4b5a6a"/></linearGradient></defs>
      <g transform="translate(817 0) scale(-1 1)">
        <path role="img" aria-label="Photo: technician servicing an open outdoor unit against a stone wall" d="M0 0H817V400C600 505 250 495 0 400Z" fill="url(#stone)"/>
        <path d="M0 420C160 480 320 505 520 500" fill="none" stroke="var(--red)" stroke-width="14"/>
        <path d="M40 410C300 515 600 495 817 415" fill="none" stroke="var(--blue)" stroke-width="16"/>
      </g>
    </svg>
    <p class="headline blue" style="left:86px;top:540px;font-size:50px;">Transparent</p>
    <p class="headline red" style="left:86px;top:598px;font-size:90px;">Pricing</p>
    <p class="body" style="left:92px;top:710px;font-size:26px;line-height:36px;">What you see is what you<br>pay—NO hidden fees!</p>
    <div class="brand" style="left:507px;top:580px;"><span class="brand__dot"></span><p class="brand__name">Brightwell Comfort Contractors</p></div>
  </section>

</div>
</body>
</html>
```